Current Employment Opportunities Email Template

We would like to redesign our internal job listing email template we send out each month. The email service we use is MailChimp and would like the template to be easy to edit when updating job postings. I attached an example below.

Font styles to use
Sans Serif

Colors

Designer to choose colors to be used in the design.

```html
<!DOCTYPE html>
<html lang="en">
<head>
<meta charset="utf-8">
<title>Today's Talent Opportunities – Harlow Services Inc.</title>
<link rel="stylesheet" href="https://fonts.googleapis.com/css2?family=Open+Sans:wght@400;600;700&family=Roboto+Condensed:wght@700&display=swap">
<style>
  :root {
    --page-bg: #f7f7f7;
    --surface: #ffffff;
    --teal: #437371;
    --teal-tint: #e9f0ef;
    --accent: #d93a06;
    --ink: #333333;
    --ink-dark: #1d1d1d;
    --card-border: #dde3e2;
  }
  * { box-sizing: border-box; margin: 0; padding: 0; }
  html, body { width: 720px; height: 1200px; overflow: hidden; }
  body {
    position: relative;
    background: var(--page-bg);
    font-family: "Open Sans", Arial, sans-serif;
    color: var(--ink);
  }
  .preheader {
    position: absolute; top: 30px; left: 0; width: 720px;
    text-align: center; font-size: 8px; color: var(--ink);
  }
  .preheader a { color: var(--teal); text-decoration: none; }

  .email {
    position: absolute; top: 54px; left: 121px; width: 478px; height: 1090px;
    background: var(--surface);
    box-shadow: 0 12px 14px -10px rgba(0,0,0,0.12);
  }
  .brand {
    color: var(--ink-dark); font-weight: 700; font-size: 20px;
    line-height: 1; white-space: nowrap;
  }
  .masthead { height: 80px; display: flex; justify-content: center; align-items: center; }

  .hero {
    position: relative; height: 113px; background: var(--teal);
    color: var(--surface); text-align: center;
  }
  .hero-title {
    font-family: "Roboto Condensed", "Arial Narrow", sans-serif;
    font-weight: 700; font-size: 30px; padding-top: 24px; line-height: 1.1;
  }
  .hero-rule { width: 392px; height: 2px; background: var(--surface); margin: 10px auto 0; }
  .hero-sub { font-size: 12.5px; margin-top: 8px; }
  .hero-arrow { position: absolute; left: 227px; bottom: -13px; }

  .intro { padding: 43px 42px 0; text-align: center; height: 218px; }
  .intro p { font-size: 11.2px; line-height: 15.4px; }

  .btn {
    display: inline-flex; align-items: center; justify-content: center;
    width: 122px; height: 33px; background: var(--accent); color: var(--surface);
    font-weight: 700; font-size: 11.5px; text-decoration: none; border-radius: 2px;
  }
  .intro .btn { margin-top: 33px; }

  .openings { background: var(--teal-tint); height: 521px; padding-top: 40px; }
  .section-title {
    font-family: "Roboto Condensed", "Arial Narrow", sans-serif; font-weight: 700;
    font-size: 26px; color: var(--teal); text-align: center; line-height: 1.2;
  }
  .job-grid {
    display: grid; grid-template-columns: 192px 192px; gap: 19px 22px;
    justify-content: center; margin-top: 21px;
  }
  .job-card {
    height: 188px; background: var(--surface); border: 1px solid var(--card-border);
    text-align: center; padding-top: 22px;
  }
  .job-city {
    font-family: "Roboto Condensed", "Arial Narrow", sans-serif; font-weight: 700;
    font-size: 22px; color: var(--teal); line-height: 1.2;
  }
  .job-title { font-size: 12.6px; margin-top: 1px; }
  .job-location { font-size: 9.8px; margin-top: 1px; }
  .job-summary {
    font-size: 9.8px; line-height: 14px; font-weight: 400; letter-spacing: 0.3px;
    color: var(--ink-dark); margin-top: 3px;
  }
  .job-card .btn { margin-top: 8px; }

  .footer { height: 158px; display: flex; flex-direction: column; align-items: center; padding-top: 50px; }
  .social { display: flex; gap: 2px; margin-top: 22px; }
</style>
</head>
<body>
  <div class="preheader">Having trouble viewing this email? <a href="#">Open in a browser window</a></div>

  <main class="email">
    <header class="masthead">
      <span class="brand">Harlow Services Inc.</span>
    </header>

    <section class="hero">
      <h1 class="hero-title">Today’s Talent Opportunities</h1>
      <div class="hero-rule"></div>
      <p class="hero-sub">Want to be a part of the most efficient and elite team in the industry?</p>
      <svg class="hero-arrow" width="24" height="13" viewBox="0 0 24 13"><polygon points="0,0 24,0 12,13" fill="#437371"/></svg>
    </section>

    <section class="intro">
      <p>We’ve got a list of opportunities here at Harlow that we’d love for you to strive for! These openings allow you to fully utilize your strengths, walk alongside us as we grow exponentially farther than we could ever dream, and leverage your successes to climb your way up the ladder of professional growth and leadership within our organization!</p>
      <a class="btn" href="#">More About Us</a>
    </section>

    <section class="openings">
      <h2 class="section-title">Current Opportunities</h2>
      <div class="job-grid">
        <article class="job-card">
          <h3 class="job-city">Dallas</h3>
          <p class="job-title">Lead Restoration Technician</p>
          <p class="job-location">Dallas, TX</p>
          <p class="job-summary">Restoration Technician in the<br>Dallas/Ft. Worth Area</p>
          <a class="btn" href="#">Learn More</a>
        </article>
        <article class="job-card">
          <h3 class="job-city">Dallas</h3>
          <p class="job-title">Lead Restoration Technician</p>
          <p class="job-location">Dallas, TX</p>
          <p class="job-summary">Restoration Technician in the<br>Dallas/Ft. Worth Area</p>
          <a class="btn" href="#">Learn More</a>
        </article>
        <article class="job-card">
          <h3 class="job-city">Dallas</h3>
          <p class="job-title">Lead Restoration Technician</p>
          <p class="job-location">Dallas, TX</p>
          <p class="job-summary">Restoration Technician in the<br>Dallas/Ft. Worth Area</p>
          <a class="btn" href="#">Learn More</a>
        </article>
        <article class="job-card">
          <h3 class="job-city">Dallas</h3>
          <p class="job-title">Lead Restoration Technician</p>
          <p class="job-location">Dallas, TX</p>
          <p class="job-summary">Restoration Technician in the<br>Dallas/Ft. Worth Area</p>
          <a class="btn" href="#">Learn More</a>
        </article>
      </div>
    </section>

    <footer class="footer">
      <span class="brand">Harlow Services Inc.</span>
      <div class="social">
        <svg width="27" height="27" viewBox="0 0 27 27" role="img" aria-label="Social profile link"><circle cx="13.5" cy="13.5" r="13" fill="#1d1d1d"/></svg>
        <svg width="27" height="27" viewBox="0 0 27 27" role="img" aria-label="Social profile link"><circle cx="13.5" cy="13.5" r="13" fill="#1d1d1d"/></svg>
      </div>
    </footer>
  </main>
</body>
</html>
```